Business Cards that are elegant and wow

I want to create and print business cards that represent my brand and stand out from the rest. We want to ensure they stay in our branding and the integrity is not lost. I am happy to look at different shapes like square etc.

It will be printed on very thick cards and will be stylish .

I want to create and print business cards that represent my brand and stand out from the rest. We want to ensure they stay in ur branding and the integrity is not lost. I am happy to look at different shapes like square etc.

Target Market(s)

real estate professionals

Industry/Entity Type

Real Estate

Contact Information for Business Card

Maren Holt
hello@brightfernrealty.com.au
brightfernrealty.com.au
0487 316 252 (SMS)

Colors

Designer to choose colors to be used in the design.

Requirements
Must have
• My logo
• email
• website
• Name
Nice to have
• I like the idea of printing with foil or spot gloss. You want it to stand out in a sea.
Should not have
• I would like you to stay in my colour themes. Don't change the colour of my logo

```html
<!DOCTYPE html>
<html lang="en">
<head>
<meta charset="utf-8">
<title>Bright Fern Realty – Business Card</title>
<link rel="stylesheet" href="https://fonts.googleapis.com/css2?family=Montserrat:wght@600&family=Roboto+Condensed:wght@300&family=Sorts+Mill+Goudy:ital@1&display=swap">
<style>
  :root {
    --cyan: #1ee8f4;
    --magenta: #ff18a6;
    --ink: #111111;
    --edge: #2a2a2a;
    --sky-top: #a9b4f2;
    --sky-mid: #e6d9f5;
    --paper: #ffffff;
    --city-blue: #5aa2e8;
    --city-light: #cfe3f7;
  }
  html, body {
    margin: 0;
    padding: 0;
    width: 995px;
    height: 1200px;
    overflow: hidden;
    background: var(--paper);
  }
  .canvas {
    position: relative;
    width: 995px;
    height: 1200px;
  }
  .card-shape {
    position: absolute;
    left: 0;
    width: 995px;
    height: 600px;
  }
  .card-front { top: 0; }
  .card-back { top: 606px; }

  .skyline {
    position: absolute;
    border-radius: 4px;
    background: linear-gradient(180deg, var(--city-light) 0%, var(--city-blue) 55%, #f2a23a 80%, #7be23c 100%);
    opacity: 0.85;
  }
  .skyline-front { left: 282px; top: 42px; width: 462px; height: 262px; }
  .skyline-back { left: 377px; top: 650px; width: 258px; height: 144px; }

  .brand {
    position: absolute;
    left: 140px;
    top: 372px;
    display: flex;
    align-items: center;
    gap: 34px;
  }
  .brand-mark {
    width: 168px;
    height: 168px;
    flex: none;
  }
  .brand-name {
    font-family: "Montserrat", sans-serif;
    font-weight: 600;
    color: var(--cyan);
    line-height: 1;
    margin: 0;
  }
  .brand-name .line-main {
    display: block;
    font-size: 76px;
    letter-spacing: -1px;
  }
  .brand-name .line-sub {
    display: block;
    font-size: 44px;
    letter-spacing: 22px;
    margin-top: 10px;
    text-align: center;
  }

  .person-name {
    position: absolute;
    left: 0;
    width: 995px;
    top: 800px;
    margin: 0;
    text-align: center;
    font-family: "Sorts Mill Goudy", serif;
    font-style: italic;
    font-size: 56px;
    color: var(--ink);
  }

  .contact-list {
    position: absolute;
    left: 244px;
    top: 924px;
    margin: 0;
    padding: 0;
    list-style: none;
  }
  .contact-item {
    display: flex;
    align-items: center;
    height: 70px;
    font-family: "Roboto Condensed", sans-serif;
    font-weight: 300;
    font-size: 37px;
    color: var(--magenta);
  }
  .contact-icon {
    width: 24px;
    height: 24px;
    margin-right: 18px;
    flex: none;
  }
</style>
</head>
<body>
<div class="canvas">

  <!-- Front of card -->
  <svg class="card-shape card-front" viewBox="0 0 995 600" aria-hidden="true">
    <defs>
      <linearGradient id="skyFront" x1="0" y1="0" x2="0" y2="1">
        <stop offset="0" stop-color="var(--sky-top)"/>
        <stop offset="0.3" stop-color="var(--sky-mid)"/>
        <stop offset="0.52" stop-color="var(--paper)"/>
        <stop offset="1" stop-color="var(--paper)"/>
      </linearGradient>
    </defs>
    <path d="M11,128 Q11,96 45,92 C200,78 350,12 497,11 C645,12 795,78 950,92 Q984,96 984,128 L984,555 Q984,583 956,583 L39,583 Q11,583 11,555 Z"
          fill="url(#skyFront)" stroke="var(--edge)" stroke-width="1"/>
  </svg>
  <div class="skyline skyline-front" role="img" aria-label="Illustrated city skyline of blue, orange and white towers on a green hill"></div>

  <div class="brand">
    <svg class="brand-mark" viewBox="0 0 168 168" aria-hidden="true">
      <circle cx="84" cy="84" r="76" fill="none" stroke="var(--cyan)" stroke-width="12"/>
    </svg>
    <h1 class="brand-name">
      <span class="line-main">BRIGHT FERN</span>
      <span class="line-sub">REALTY</span>
    </h1>
  </div>

  <!-- Back of card -->
  <svg class="card-shape card-back" viewBox="0 0 995 600" aria-hidden="true">
    <defs>
      <linearGradient id="skyBack" x1="0" y1="0" x2="0" y2="1">
        <stop offset="0" stop-color="var(--sky-top)"/>
        <stop offset="0.35" stop-color="var(--sky-mid)"/>
        <stop offset="0.6" stop-color="var(--paper)"/>
        <stop offset="1" stop-color="var(--paper)"/>
      </linearGradient>
    </defs>
    <path d="M11,128 Q11,96 45,92 C200,78 350,12 497,11 C645,12 795,78 950,92 Q984,96 984,128 L984,554 Q984,582 956,582 L39,582 Q11,582 11,554 Z"
          fill="url(#skyBack)" stroke="var(--edge)" stroke-width="1"/>
  </svg>
  <div class="skyline skyline-back" role="img" aria-label="Small illustrated city skyline on a green hill"></div>

  <p class="person-name">Maren Holt</p>

  <ul class="contact-list">
    <li class="contact-item">
      <svg class="contact-icon" viewBox="0 0 24 24" aria-hidden="true">
        <rect x="1" y="4" width="22" height="16" fill="var(--cyan)"/>
        <path d="M1,4 L12,13 L23,4 M1,20 L9,11 M23,20 L15,11" fill="none" stroke="var(--paper)" stroke-width="1.8"/>
      </svg>
      hello@brightfernrealty.com.au
    </li>
    <li class="contact-item">
      <svg class="contact-icon" viewBox="0 0 24 24" aria-hidden="true">
        <circle cx="11" cy="11" r="9" fill="none" stroke="var(--cyan)" stroke-width="2.4"/>
        <path d="M2,11 H20 M11,2 V20 M11,2 C6,7 6,15 11,20 M11,2 C16,7 16,15 11,20" fill="none" stroke="var(--cyan)" stroke-width="1.4"/>
        <path d="M17,17 L23,23" stroke="var(--cyan)" stroke-width="2.6"/>
      </svg>
      brightfernrealty.com.au
    </li>
    <li class="contact-item">
      <svg class="contact-icon" viewBox="0 0 24 24" aria-hidden="true">
        <path d="M6.6,2 L9.5,6.5 L7.6,8.8 C8.8,11.6 11.4,14.4 14.6,16 L16.8,14 L21.5,16.8 L19.6,21 C12,21 3,12.5 3,4.4 Z" fill="var(--cyan)"/>
      </svg>
      0487 316 252 (SMS)
    </li>
  </ul>

</div>
</body>
</html>
```